Vantrell Law Letterhead

We need a new letterhead design for a Law Firm. The address for the law firm is 4817 Larkspur Boulevard, Suite 250, Houston, Texas 77342. Phone Number: 832-619-3057; Fax Number: 832-407-1694. The logo is uploaded to the project.

```html
<!DOCTYPE html>
<html lang="en">
<head>
<meta charset="utf-8">
<title>Vantrell Law Letterhead</title>
<link href="https://fonts.googleapis.com/css2?family=Mulish:wght@300;400;600;700;800&display=swap" rel="stylesheet">
<style>
  :root {
    --backdrop: #e7e7e7;
    --paper: #ffffff;
    --navy: #1f3769;
    --red: #c8242d;
    --ink: #1e1e1e;
    --muted: #555a63;
    --watermark: #ebeaec;
  }
  * { margin: 0; padding: 0; box-sizing: border-box; }
  html, body {
    width: 1200px; height: 904px; overflow: hidden;
    background: var(--backdrop);
    font-family: "Mulish", sans-serif;
  }
  .letterhead {
    position: absolute; left: 268px; top: 22px;
    width: 664px; height: 860px;
    background: var(--paper);
    box-shadow: 0 1px 4px rgba(0,0,0,0.08);
    overflow: hidden;
  }
  .brand {
    position: absolute; left: 39px; top: 44px;
    display: flex; align-items: center; gap: 10px;
  }
  .brand-dot { width: 40px; height: 40px; border-radius: 50%; background: var(--navy); }
  .brand-name {
    font-size: 28px; font-weight: 700; color: var(--navy);
    letter-spacing: 0.3px; line-height: 1;
  }
  .contact {
    position: absolute; left: 462px; top: 40px;
    font-size: 11px; font-weight: 300; color: var(--muted); line-height: 13.5px;
  }
  .contact-line { display: flex; align-items: center; gap: 7px; margin-top: 2px; }
  .contact-line:first-of-type { margin-top: 5px; }
  .contact-icon { width: 10px; height: 10px; flex: none; }
  .subject { position: absolute; left: 46px; top: 176px; color: var(--ink); }
  .subject-label { font-size: 8px; font-weight: 700; }
  .subject-title { font-size: 11px; font-weight: 800; margin-top: 3px; }
  .body-copy {
    position: absolute; left: 46px; top: 250px; width: 460px;
    font-size: 7.1px; font-weight: 600; color: var(--ink); line-height: 14.2px;
  }
  .body-copy p + p { margin-top: 14.2px; }
  .watermark {
    position: absolute; left: 42px; top: 592px;
    width: 226px; height: 226px; border-radius: 50%;
    background: var(--watermark);
  }
  .sign-off { position: absolute; left: 359px; top: 600px; color: var(--ink); }
  .signer-name { font-size: 7px; font-weight: 700; }
  .signer-role { font-size: 5.5px; font-weight: 700; margin-top: 2px; }
  .signature {
    position: absolute; left: 18px; top: 4px; width: 78px; height: 50px;
    background: linear-gradient(135deg, rgba(40,40,40,0.05), rgba(40,40,40,0.12));
  }
</style>
</head>
<body>
  <main class="letterhead">
    <header>
      <div class="brand">
        <span class="brand-dot"></span>
        <span class="brand-name">Vantrell Law</span>
      </div>
      <address class="contact" style="font-style:normal">
        <div>4817 Larkspur Boulevard,</div>
        <div>Suite 250, Houston, Texas 77342</div>
        <div class="contact-line">
          <svg class="contact-icon" viewBox="0 0 10 10" aria-hidden="true">
            <circle cx="5" cy="5" r="5" fill="#c8242d"/>
            <path d="M3.2 2.6c.3-.3.7-.2.9.1l.5.8c.1.3 0 .5-.2.7l-.3.2c.3.7.8 1.2 1.5 1.5l.2-.3c.2-.2.5-.3.7-.2l.8.5c.3.2.4.6.1.9l-.4.4c-1.6.3-4.3-2.4-4-4z" fill="#fff"/>
          </svg>
          <span>832-619-3057</span>
        </div>
        <div class="contact-line">
          <svg class="contact-icon" viewBox="0 0 10 10" aria-hidden="true">
            <circle cx="5" cy="5" r="5" fill="#c8242d"/>
            <rect x="3" y="2.5" width="4" height="2" fill="#fff"/>
            <rect x="2.5" y="4.8" width="5" height="2.8" rx="0.4" fill="#fff"/>
          </svg>
          <span>832-407-1694</span>
        </div>
      </address>
    </header>

    <section class="subject">
      <div class="subject-label">Subject :</div>
      <div class="subject-title">Nunc pretium nibh in elit blandit a aliquet</div>
    </section>

    <section class="body-copy">
      <p>Lorem ipsum dolor sit amet, consectetur adipiscing elit. Nunc pretium nibh in elit blandit a aliquet lacus tempus. Nam in leo justo. Integer condimentum venenatis dapibus. Pellentesque sit amet est arcu, a adipiscing tortor.</p>
      <p>In nisi lectus, euismod nec sodales sed, blandit et dui. In nec nulla lectus, non laoreet metus. Nullam neque metus, adipiscing non aliquam ac, adipiscing sit amet elit. Proin commodo porta condimentum. In pulvinar lacinia est, non feugiat nisl vehicula quis. Nunc bibendum facilisis elementum. Duis ut dolor quis mi aliquet dapibus. Maecenas sodales leo sed lacus laoreet volutpat. Nullam aliquam tempor consequat.</p>
      <p>Integer eu est id libero accumsan euismod. Nunc quis sagittis magna. Duis vulputate, nibh sit amet lobortis condimentum, tortor ligula faucibus nulla, eget fringilla justo quam non purus. Mauris eu dictum orci. In hac habitasse platea dictumst. Vestibulum enim nisl, viverra non condimentum quis, molestie eget ante. Praesent volutpat vestibulum nulla vestibulum aliquet. Fusce elementum, lacus eget mattis placerat, nisi dolor varius erat, eu vulputate lorem metus vitae lorem. Praesent ipsum quam, sollicitudin nec elementum sit amet, feugiat nec odio. Phasellus et justo elit, eu consequat diam. Quisque euismod laoreet enim nec tincidunt. Nulla facilisi. In molestie, lacus quis gravida auctor, justo dolor elementum tortor, eu fringilla augue nisi nec tellus. Sed aliquet tempor fermentum. In nisi lectus, euismod nec sodales sed, blandit et dui. In nec nulla lectus, non laoreet metus. Nullam neque metus, adipiscing non aliquam ac, adipiscing sit amet elit. Proin commodo porta condimentum. In pulvinar lacinia est, non feugiat nisl vehicula quis. Nunc bibendum facilisis elementum. Duis ut dolor quis mi aliquet dapibus. Maecenas sodales leo sed lacus laoreet volutpat. Nullam aliquam tempor consequat.</p>
      <p>Integer eu est id libero accumsan euismod. Nunc quis sagittis magna. Duis vulputate, nibh sit amet lobortis condimentum, tortor ligula faucibus nulla, eget fringilla justo quam non purus. Integer eu est id libero accumsan euismod. Nunc quis sagittis magna. Duis vulputate, nibh sit amet lobortis condimentum, tortor ligula faucibus nulla, eget fringilla justo quam non purus.</p>
    </section>

    <div class="watermark" aria-hidden="true"></div>

    <footer class="sign-off">
      <div class="signer-name">Orla Benedikt</div>
      <div class="signer-role">Manager</div>
      <div class="signature" role="img" aria-label="Handwritten signature of the manager"></div>
    </footer>
  </main>
</body>
</html>
```